Web Design Project

This is a wordpress project for a newly formed biologics company based in the US with international clientele. We do manufacturing of biologically based raw materials using a state of the art facility....Our logo must be incorporated....logo colors Navy and Gray. It is fine to use some color in web design. The viewer will primarily be industry folk.

Velorast Biologics, LLC is a contract manufacturing organization which produces biologically-based raw materials derived primarily from human plasma. The company services include extraction and purification of plasma components, especially proteins and enzymes. The business focuses on biotherapeutics, diagnostic and veterinary markets worldwide.

5 pages a bad example of first page can be found in attached files.....
use stock photos of labs and clean rooms.
Updates

Project Deadline Extended
Reason: I need a bit more time tonprovide feedback.

Project Deadline Extended
Reason: needed time to evaluate existing options

Target Market(s)

target market Pharmaceutical companies and research universities

Industry/Entity Type

Veterinary

Requirements
Must have
• our logo...we will provide some graphics...

```html
<!DOCTYPE html>
<html lang="en">
<head>
<meta charset="utf-8">
<title>Velorast Biologics</title>
<link rel="stylesheet" href="https://fonts.googleapis.com/css2?family=Source+Sans+3:wght@400;600&family=Noto+Sans:wght@400&display=swap">
<style>
  :root {
    --navy: #0d3f7a;
    --navy-deep: #0b3a72;
    --gray-text: #555b61;
    --heading: #0f4a86;
    --header-top: #f3f7fb;
    --header-bottom: #dde6ef;
    --band: #e6ebf0;
    --rule: #b9c4cf;
    --white: #ffffff;
  }
  * { box-sizing: border-box; margin: 0; padding: 0; }
  html, body { width: 1182px; height: 1200px; overflow: hidden; }
  body {
    position: relative;
    background: linear-gradient(to bottom, var(--navy) 0, var(--navy) 113px, #e1e8ef 113px, #ffffff 330px, #ffffff 100%);
    font-family: "Noto Sans", sans-serif;
    color: var(--gray-text);
  }
  .search {
    position: absolute; left: 943px; top: 14px; width: 192px; height: 28px;
    background: var(--white); border: 1px solid #c9d2db; border-radius: 3px;
    font: 400 13px "Source Sans 3", sans-serif; color: #8a9199;
    padding: 5px 10px;
  }
  .search svg { position: absolute; right: 7px; top: 7px; }
  .site-header {
    position: absolute; left: 47px; top: 56px; width: 1089px; height: 124px;
    background: linear-gradient(to bottom, var(--header-top), var(--header-bottom));
    border-radius: 4px 4px 0 0;
    border-bottom: 3px solid #b4c3d2;
  }
  .brand {
    position: absolute; left: 26px; top: 12px; height: 92px;
    display: flex; align-items: center; gap: 10px;
  }
  .brand-mark { width: 90px; height: 90px; border-radius: 50%; background: var(--navy); }
  .brand-name { font: 600 34px "Source Sans 3", sans-serif; color: var(--navy); letter-spacing: -0.3px; }
  .main-nav {
    position: absolute; right: 22px; top: 46px;
    display: flex; font: 400 17px "Source Sans 3", sans-serif; color: #2c3640;
  }
  .main-nav span { padding: 0 14px; }
  .main-nav .sep { padding: 0 8px; color: #3a434c; }
  .main-nav .current { color: var(--navy); }
  .hero {
    position: absolute; left: 47px; top: 182px; width: 1089px; height: 381px;
    background: linear-gradient(100deg, #e6ecf3 0%, #dbe3ec 45%, #ced8e2 62%, #e9eef3 78%, #d7dde3 100%);
    border-bottom: 3px solid #b4c3d2;
  }
  .hero-title { position: absolute; left: 161px; top: 298px; font: 400 32px "Source Sans 3", sans-serif; color: var(--navy); }
  .hero-sub { position: absolute; left: 161px; top: 352px; font: 400 22px "Source Sans 3", sans-serif; color: #4a4f55; }
  .pager {
    position: absolute; left: 63px; top: 506px; width: 133px; height: 34px;
    background: #3d3f42; border-radius: 17px;
  }
  .column { position: absolute; top: 606px; width: 330px; }
  .column h2 { font: 400 26px "Source Sans 3", sans-serif; color: var(--heading); margin-bottom: 12px; }
  .column p { font-size: 12.6px; line-height: 20.3px; letter-spacing: 0.6px; text-align: justify; }
  .column .more { color: var(--navy); }
  .col-welcome { left: 48px; }
  .col-welcome p { margin-top: 2px; }
  .col-lab { left: 424px; }
  .col-research { left: 805px; }
  .thumb {
    width: 315px; height: 118px; border: 1px solid #b9bec4; margin: 4px 0 16px 7px;
  }
  .thumb-lab { background: linear-gradient(to right, #c7ccd0, #e8ebee 40%, #d0d5da 70%, #b8bec5); }
  .thumb-research { background: linear-gradient(to right, #eef3f8, #dfe8f1 60%, #cfd8e1); }
  .feature-band {
    position: absolute; left: 0; top: 912px; width: 1182px; height: 187px;
    background: var(--band); border-top: 2px dashed var(--rule);
  }
  .feature-image {
    position: absolute; left: 70px; top: 29px; width: 175px; height: 134px;
    border: 3px solid #b7bcc2;
    background: radial-gradient(circle at 40% 45%, #e0262b, #b1121a 55%, #6d060b);
  }
  .feature-title { position: absolute; left: 272px; top: 29px; font-size: 16.5px; letter-spacing: 0.5px; color: #222; }
  .feature-text {
    position: absolute; left: 274px; top: 66px; width: 850px;
    font-size: 15px; line-height: 22.5px; letter-spacing: 0.5px; color: var(--navy);
  }
  .site-footer {
    position: absolute; left: 0; top: 1099px; width: 1182px; height: 101px;
    background: var(--navy-deep); color: var(--white);
    font: 400 13px "Source Sans 3", sans-serif;
  }
  .footer-nav { position: absolute; left: 48px; top: 22px; display: flex; }
  .footer-nav .sep { padding: 0 17px; }
  .copyright { position: absolute; left: 48px; top: 57px; }
  .connect { position: absolute; left: 978px; top: 22px; }
  .social { position: absolute; left: 977px; top: 51px; display: flex; gap: 5px; }
  .social span { width: 27px; height: 27px; border-radius: 50%; background: var(--white); }
</style>
</head>
<body>
  <div class="search">Search
    <svg width="13" height="13" viewBox="0 0 13 13"><circle cx="5" cy="5" r="3.8" fill="none" stroke="#666" stroke-width="1.5"/><line x1="8" y1="8" x2="12" y2="12" stroke="#666" stroke-width="2"/></svg>
  </div>

  <header class="site-header">
    <div class="brand">
      <div class="brand-mark"></div>
      <div class="brand-name">Velorast Biologics</div>
    </div>
    <nav class="main-nav">
      <span class="current">Home</span><span class="sep">|</span>
      <span>Laboratory</span><span class="sep">|</span>
      <span>Research</span><span class="sep">|</span>
      <span>Team</span><span class="sep">|</span>
      <span>Contact Us</span>
    </nav>
  </header>

  <div class="hero" role="img" aria-label="Smiling scientist in a lab coat with a colleague working in a bright laboratory behind her"></div>
  <div class="hero-title">Nostrum exercitationem</div>
  <div class="hero-sub">velit esse quam nihil molestiae consequatur</div>
  <div class="pager">
    <svg width="133" height="34" viewBox="0 0 133 34">
      <polyline points="18,11 13,17 18,23" fill="none" stroke="#fff" stroke-width="2.5"/>
      <circle cx="34" cy="17" r="3.5" fill="#fff"/>
      <circle cx="50" cy="17" r="3.5" fill="#111"/>
      <circle cx="67" cy="17" r="3.5" fill="#fff"/>
      <circle cx="83" cy="17" r="3.5" fill="#fff"/>
      <circle cx="99" cy="17" r="3.5" fill="#fff"/>
      <polyline points="114,11 119,17 114,23" fill="none" stroke="#fff" stroke-width="2.5"/>
    </svg>
  </div>

  <section class="column col-welcome">
    <h2>Welcome</h2>
    <p>Nemo enim ipsam voluptatem quia voluptas sit aspernatur aut odit aut fugit, sed quia consequuntur magni dolores eos qui ratione voluptatem sequi nesciunt. Neque porro quisquam est, qui dolorem ipsum quia dolor sit amet, consectetur, adipisci velit, sed quia non numquam eius modi tempora incidunt ut labore et dolore magnam aliquam quaerat voluptatem. Ut enim ad minima veniam, quis nostrum exercitationem ullam corporis suscipit laboriosam, nisi ut aliquid ex ea commodi consequatur <span class="more">More...</span></p>
  </section>

  <section class="column col-lab">
    <h2>Laboratory</h2>
    <div class="thumb thumb-lab" role="img" aria-label="Clean laboratory room with a fume hood and sink"></div>
    <p>Ut enim ad minima veniam, quis nostrum exercitationem ullam corporis suscipit laboriosam, nisi ut aliquid ex ea commodi consequatur quis autem vel eum <span class="more">More...</span></p>
  </section>

  <section class="column col-research">
    <h2>Research</h2>
    <div class="thumb thumb-research" role="img" aria-label="Researcher viewed through glass petri dishes"></div>
    <p>Neque porro quisquam est, qui dolorem ipsum quia dolor sit amet, consectetur, adipisci velit, sed quia non numquam eius modi tempora incidunt ut labore et dolore magnam. <span class="more">More...</span></p>
  </section>

  <section class="feature-band">
    <div class="feature-image" role="img" aria-label="Close view of red blood cells"></div>
    <div class="feature-title">Human Plasmas</div>
    <p class="feature-text">Nemo enim ipsam voluptatem quia voluptas sit aspernatur aut odit aut fugit, sed quia consequuntur magni dolores eos qui ratione voluptatem sequi nesciunt. Neque porro quisquam est, qui dolorem ipsum quia dolor sit amet, consectetur, adipisci velit, sed quia non numquam eius modi tempora incidunt abore et dolore magnam aliquam quaerat voluptatem.</p>
  </section>

  <footer class="site-footer">
    <nav class="footer-nav">
      <span>Home</span><span class="sep">|</span>
      <span>Laboratory</span><span class="sep">|</span>
      <span>Research</span><span class="sep">|</span>
      <span>Team</span><span class="sep">|</span>
      <span>Contact Us</span><span class="sep">|</span>
      <span>Sitemap</span>
    </nav>
    <div class="copyright">Copyright © 2012 www.velorastbiologics.com &nbsp; All rights reserved</div>
    <div class="connect">Connect with us :</div>
    <div class="social"><span></span><span></span><span></span><span></span><span></span></div>
  </footer>
</body>
</html>
```